Ecommerce brand for entrepreneurs needs help with branding products

I am looking for help to design a small supplement pouch. Including colours, layout and design.

The business:
The business is called 'Keel Orbit' and our goal is to help entrepreneurs continue to change the world in spite of how difficult it is.

At Keel Orbit, we understand being an entrepreneur is one of the hardest jobs there is. We believe there is a better way. A way in which you don’t have to choose between success in your business and the rest of your life. Our aim is to solve these challenges, so you can stay in the fight a little longer. If we can do this, we can ultimately change the world into a better place.

We will do this through a range of supplements, community, information and physical products to help you optimise their lives.

The product:
The product I am looking to create is for a natural nootropic called

‘The Velvet Compass’

The product will address the challenges with focus and lower attention spans.

So Entrepreneurs can Solve more problems, Help more people and make more money.

Do more in four hours than a whole day. Have Zen like calm. With Zero Jitters & Zero Crashes. Do what others can’t

The design:
I want this to be a small pouch. The final design should be elegant, and minimalist and have an edge that is different.

I have added examples of products that I like below.

I am open to most colour combinations but silver, navy, black, orange, white and translucent are what is taking my fancy right now.

I like the idea of having a translucent package or part of the package like some of the designs below. I also like the matt finish of some of the designs along with the flashes of shininess from silver for contrast. or even using embossing within the packaging.

I have a logo that I have made but I am open to changes on that as well if you see fit. if you do want to do this, I would love to see an emblem next to the words Keel Orbit that encapsulates the brand.

I have done some really really rough mockups myself but would like to see what you have to offer rather than what I have done

The purpose of this image:
I need a 3D mockup of this supplement to be on my landing page to start to take pre-orders.

I am ideally looking for 2 images

1) Supplement packaging on its own
2) Supplement packaging with background coloured lighting, with powder on the ground etc

Need extra days to review

Target Market(s)

The logo: Please also redesign my logo - I would love to see an emblem next to the words Keel Orbit that encapsulates the brand.The business is called 'Keel Orbit' and our goal is to help entrepreneurs continue to change the world in spite of how difficult it is. At Keel Orbit, we understand being an entrepreneur is one of the hardest jobs there is. We believe there is a better way. A way in which you don’t have to choose between success in your business and the rest of your life. Our aim is to solve these challenges, so you can stay in the fight a little longer. If we can do this, we can ultimately change the world into a better place. We will do this through a range of supplements, community, information and physical products to help you optimise their lives.

Industry/Entity Type

Supplements for entrepreneurs

Colors

Requirements
Must have
• The design: I want this to be a small pouch. The final design should be elegant, and minimalist and have an edge that is different. I have added examples of products that I like below. I am open to most colour combinations but silver, navy, black, orange, white and translucent are what is taking my fancy right now. I like the idea of having a translucent package or part of the package like some of the designs below. I also like the matt finish of some of the designs along with the flashes of shininess from silver for contrast. or even using embossing within the packaging.

```html
<!DOCTYPE html>
<html lang="en">
<head>
<meta charset="utf-8">
<title>Keel Orbit – The Velvet Compass pouch</title>
<link rel="stylesheet" href="https://fonts.googleapis.com/css2?family=Quicksand:wght@400;500;700&display=swap">
<style>
  :root {
    --backdrop: #949494;
    --pouch-orange: #d27a36;
    --pouch-orange-light: #de9458;
    --pouch-orange-deep: #c8692a;
    --ink-white: #f6efe8;
    --ornament-line: rgba(246, 230, 212, 0.35);
    --band: rgba(240, 200, 160, 0.6);
  }
  * { box-sizing: border-box; margin: 0; padding: 0; }
  html, body {
    width: 1200px;
    height: 800px;
    overflow: hidden;
    background: var(--backdrop);
    font-family: "Quicksand", sans-serif;
  }
  .canvas {
    position: relative;
    width: 1200px;
    height: 800px;
  }
  .pouch {
    position: absolute;
    left: 390px;
    top: 80px;
    width: 420px;
    height: 650px;
    border-radius: 18px;
    background: linear-gradient(160deg, var(--pouch-orange-light) 0%, var(--pouch-orange) 45%, var(--pouch-orange-deep) 100%);
    color: var(--ink-white);
    overflow: hidden;
  }
  .pouch-ornament {
    position: absolute;
    left: 0;
    top: 0;
    width: 420px;
    height: 156px;
    background: radial-gradient(ellipse 60% 100% at 50% 0%, rgba(236, 170, 112, 0.75) 0%, rgba(222, 148, 88, 0.35) 60%, rgba(210, 122, 54, 0) 100%);
  }
  .zip-seal {
    position: absolute;
    left: 24px;
    right: 24px;
    top: 86px;
    height: 4px;
    border-top: 1px solid var(--ornament-line);
    border-bottom: 1px solid var(--ornament-line);
  }
  .brand {
    position: absolute;
    left: 62px;
    top: 208px;
    display: flex;
    align-items: center;
    gap: 14px;
  }
  .brand-dot {
    width: 40px;
    height: 40px;
    border-radius: 50%;
    border: 4px solid var(--ink-white);
  }
  .brand-name {
    font-size: 33px;
    font-weight: 700;
    letter-spacing: 1px;
    text-transform: uppercase;
  }
  .product-name {
    position: absolute;
    left: 60px;
    top: 336px;
    font-size: 29px;
    font-weight: 700;
    letter-spacing: 0.5px;
    white-space: nowrap;
  }
  .title-band {
    position: absolute;
    left: 0;
    top: 358px;
  }
  .tagline {
    position: absolute;
    right: 66px;
    top: 370px;
    font-size: 15px;
    font-weight: 500;
    letter-spacing: 0.5px;
  }
  .flavour {
    position: absolute;
    left: 60px;
    top: 394px;
    font-size: 15px;
    font-weight: 700;
    letter-spacing: 0.5px;
  }
  .audience {
    position: absolute;
    left: 0;
    right: 0;
    top: 464px;
    text-align: center;
    font-size: 13.5px;
    font-weight: 500;
    letter-spacing: 0.4px;
  }
  .benefits {
    position: absolute;
    left: 0;
    right: 0;
    top: 490px;
    text-align: center;
    font-size: 19px;
    font-weight: 700;
    letter-spacing: 0.6px;
  }
  .category {
    position: absolute;
    left: 0;
    right: 0;
    top: 592px;
    text-align: center;
    font-size: 13px;
    font-weight: 500;
    letter-spacing: 0.5px;
  }
</style>
</head>
<body>
  <main class="canvas">
    <section class="pouch">
      <div class="pouch-ornament" role="img" aria-label="Fine-line orange slice ornament across the top of the pouch"></div>
      <div class="zip-seal"></div>

      <div class="brand">
        <span class="brand-dot"></span>
        <span class="brand-name">Keel Orbit</span>
      </div>

      <svg class="title-band" width="180" height="30" viewBox="0 0 180 30" aria-hidden="true">
        <path d="M0 2 Q70 14 160 18" fill="none" stroke="var(--band)" stroke-width="6"/>
      </svg>
      <h1 class="product-name">The Velvet Compass</h1>
      <p class="tagline">Do What Others Can’t</p>
      <p class="flavour">Orange &amp; Mango Flavour</p>

      <p class="audience">Specifically For Founders &amp; Entrepreneurs</p>
      <p class="benefits">Focus | Flow | Drive</p>

      <p class="category">Natural Nootropic</p>
    </section>
  </main>
</body>
</html>
```